Need Power Point Presentation - That incorporates New Logo

We have a new logo and would like to incorporate it into a Power Point template. We are looking for title page, 2 body pages and a closing page design. If you have any questions please let me know. New logo is attached.

```html
<!DOCTYPE html>
<html lang="en">
<head>
<meta charset="utf-8">
<title>Lumera presentation template</title>
<link href="https://fonts.googleapis.com/css2?family=Cinzel:wght@600;700&family=Crimson+Text:wght@400;600&family=Open+Sans:wght@400;600;700&display=swap" rel="stylesheet">
<style>
:root{
  --board:#000;
  --paper:#fff;
  --ink:#1f2b36;
  --body:#333c44;
  --blue:#1e88d8;
  --blue-deep:#1b6fb8;
  --blue-mid:#4aa3dd;
  --blue-soft:#8fc6ec;
  --blue-pale:#d7ebf8;
  --row-a:#3f9be0;
  --row-b:#2f8cd6;
}
*{box-sizing:border-box;margin:0;padding:0}
html,body{width:929px;height:1200px;overflow:hidden;background:var(--board)}
.board{position:relative;width:929px;height:1200px}
.slide{position:absolute;width:295px;height:223px;background:var(--paper);overflow:hidden;font-family:"Crimson Text",serif;color:var(--body)}
.c1{left:14px}.c2{left:317px}.c3{left:620px}
.r1{top:15px}.r2{top:252px}.r3{top:488px}.r4{top:724px}.r5{top:960px}
.title{position:absolute;left:34px;top:18px;font:600 8px "Cinzel",serif;color:var(--ink);letter-spacing:.2px;white-space:nowrap}
.rule{position:absolute;left:6px;width:24px;height:1px;background:var(--blue-soft)}
.footer{position:absolute;left:0;right:5px;bottom:8px;height:18px;background:linear-gradient(90deg,var(--blue-pale),var(--blue-soft) 55%,var(--blue-mid));border-radius:0 9px 9px 0}
.footer .page{position:absolute;left:20px;top:5px;font:400 4px "Open Sans",sans-serif;color:#fff}
.footer .url{position:absolute;left:46px;top:5px;font:400 4.5px "Open Sans",sans-serif;color:#fff}
.brand{font-family:"Open Sans",sans-serif;font-weight:600;letter-spacing:.5px}
.footer .brand{position:absolute;right:12px;top:3px;font-size:9px;color:#fff}
.txt{position:absolute;font-size:4.3px;line-height:5.2px;text-align:justify;color:var(--body)}
.txt p+p{margin-top:5px}
.photo{position:absolute}
/* cover slides */
.cover{background:linear-gradient(180deg,#d9eefa,#9fd0f0 45%,#5fb0e6)}
.cover .pill{position:absolute;left:-40px;top:52px;width:330px;height:110px;border-radius:55px;background:linear-gradient(180deg,#6cb6ea,#2f8bd6)}
.cover .pill.light{background:linear-gradient(180deg,#eef8fd,#b3dbf4)}
.cover > .brand{position:absolute;left:22px;top:20px;font-size:10px;color:#fff}
.cover h1{position:absolute;left:24px;font:700 15px "Open Sans",sans-serif;color:#fff;white-space:nowrap}
.cover h1.serif{font:700 15px "Cinzel",serif}
.cover h2{position:absolute;left:24px;font:700 5px "Open Sans",sans-serif;color:var(--blue-deep);white-space:nowrap}
.cover .small{position:absolute;left:24px;font:400 4px "Open Sans",sans-serif;color:#e6f3fb}
.cover .footer{background:linear-gradient(90deg,rgba(255,255,255,0),rgba(255,255,255,.3))}
/* numbered items */
.item{position:absolute}
.item .num{position:absolute;left:0;top:0;width:10px;height:10px;background:var(--blue);color:#fff;font:400 4.5px "Open Sans",sans-serif;text-align:center;line-height:10px}
.item h3{position:absolute;left:17px;top:1px;font:600 5.5px "Cinzel",serif;color:var(--ink);white-space:nowrap}
.item .line{position:absolute;left:17px;top:9px;height:.7px;background:var(--blue)}
.item .txt{left:17px;top:12px}
/* tables */
table{position:absolute;border-collapse:collapse;font:400 3.4px "Open Sans",sans-serif;color:#fff}
th{background:var(--blue-deep);font-weight:700;padding:2px 3px;text-align:left}
td{padding:2.2px 3px}
tr:nth-child(odd) td{background:var(--row-a)}
tr:nth-child(even) td{background:var(--row-b)}
.lead{position:absolute;left:0;right:0;text-align:center;font:400 6px "Open Sans",sans-serif;color:#111}
.bullets{position:absolute;left:165px;top:50px;list-style:none;font-size:4.4px;line-height:9.2px;color:var(--body)}
.bullets li::before{content:"";display:inline-block;width:3.5px;height:3.5px;background:var(--blue-mid);margin-right:7px;vertical-align:0}
.legend{position:absolute;font:400 3.2px "Open Sans",sans-serif;color:#555;white-space:nowrap}
.legend i{display:inline-block;width:3px;height:3px;margin:0 1.5px 0 3px;vertical-align:-.3px}
</style>
</head>
<body>
<main class="board">

<!-- 1 logo slide -->
<section class="slide c1 r1" style="background:radial-gradient(circle at 50% 45%,#fff,#eeeff1)">
  <div class="brand" style="position:absolute;left:88px;top:92px;font-size:24px;color:var(--blue-mid)">LUMERA</div>
  <div style="position:absolute;left:124px;top:202px;font:400 4.5px 'Open Sans',sans-serif;color:#333">www.lumera-deck.com</div>
</section>

<!-- 2 title slide -->
<section class="slide c2 r1 cover">
  <div class="brand">LUMERA</div>
  <div class="pill"></div>
  <h1 class="serif" style="top:96px">PRESENTATION TITTLE HERE</h1>
  <h2 style="top:118px">YOUR PRESENTATION SUB TITLE HERE</h2>
  <div class="small" style="top:196px">© 2013 LUMERA. ALL RIGHTS RESERVED</div>
</section>

<!-- 3 mission 1 -->
<section class="slide c3 r1">
  <div class="rule" style="top:21px"></div><div class="rule" style="top:24px"></div>
  <div class="title">Concept plus presentation powerful mission 1</div>
  <div class="photo" role="img" aria-label="Photo of a lit glass office tower at dusk" style="left:35px;top:42px;width:65px;height:115px;background:linear-gradient(180deg,#1d2a45,#3a5a86 55%,#c98a4a)"></div>
  <div class="txt" style="left:148px;top:52px;width:137px">
    <p>The HCRF has forged a courageous and dynamic approach to the methodology of cancer research. By overcoming previous pitfalls that held the industry back, the HCRF has propelled the frontier of multiple myeloma research to a new level.</p>
    <p>Essential to this approach are 4 reviews pitfalls that held the industry back, the HCRF has propelled the frontier of multiple myeloma research to a new level, groundbreaking initiatives that have revolutionized the way research and drug development are conducted. With these models, the HCRF can dramatically accelerate.</p>
    <p>Groundbreaking initiatives that have revolutionized the way research and drug development are conducted.</p>
  </div>
  <div class="footer"><span class="url">www.lumera-deck.com</span><span class="brand">LUMERA</span></div>
</section>

<!-- 4 mission 2 -->
<section class="slide c1 r2">
  <div class="title">Concept plus presentation powerful mission 2</div>
  <div class="photo" role="img" aria-label="Photo of three smiling business people" style="left:35px;top:50px;width:65px;height:45px;background:linear-gradient(180deg,#e9edf2,#8a96a8 60%,#2c3440)"></div>
  <div class="txt" style="left:35px;top:110px;width:108px">
    <p>The HCRF has forged a courageous and dynamic approach to the methodology of cancer research.</p>
    <p>By overcoming previous pitfalls that held the industry back, the HCRF has propelled the frontier of multiple myeloma research to a new level. Groundbreaking initiatives that have revolutionized the way research and drug development are conducted.</p>
  </div>
  <div class="txt" style="left:152px;top:50px;width:133px">
    <p>The HCRF has forged a courageous and dynamic approach to the methodology of cancer research. By overcoming previous pitfalls that held the industry back, the HCRF has propelled the frontier of multiple myeloma research to a new level.</p>
    <p>Essential to this approach are 4 reviews pitfalls that held the industry back, the HCRF has propelled the frontier of multiple myeloma research to a new level, groundbreaking initiatives that have revolutionized the way research and drug development are conducted. With these models, the HCRF can dramatically accelerate.</p>
    <p>Groundbreaking initiatives that have revolutionized the way research and drug development are conducted.</p>
  </div>
  <div class="footer"><span class="page">2</span><span class="url">www.lumera-deck.com</span><span class="brand">LUMERA</span></div>
</section>

<!-- 5 mission 3 -->
<section class="slide c2 r2">
  <div class="title">Concept plus presentation powerful mission 3</div>
  <div class="item" style="left:33px;top:48px"><span class="num">1</span><h3>We know firsthand 1</h3><span class="line" style="width:230px"></span>
    <div class="txt" style="width:230px">Since 1998, we have supported thousands of patients from the point of diagnosis through their journey with the disease. we have supported thousands of patients from the point.</div></div>
  <div class="item" style="left:33px;top:90px"><span class="num">2</span><h3>We know firsthand 2</h3><span class="line" style="width:230px"></span>
    <div class="txt" style="width:230px">They have supported thousands of patients from the point of diagnosis through their journey with the disease. we have supported thousands of patients from the point. By overcoming previous pitfalls that held the industry back, the HCRF has propelled the frontier of multiple myeloma research to a new level.</div></div>
  <div class="item" style="left:33px;top:138px"><span class="num">3</span><h3>We know firsthand 3</h3><span class="line" style="width:230px"></span>
    <div class="txt" style="width:230px">We have supported thousands of patients from the point of diagnosis through their journey with the disease. we have supported thousands of patients from the point held the industry.</div></div>
  <div class="footer"><span class="page">3</span><span class="url">www.lumera-deck.com</span><span class="brand">LUMERA</span></div>
</section>

<!-- 6 mission 4 -->
<section class="slide c3 r2">
  <div class="title">Concept plus presentation powerful mission 4</div>
  <div class="item" style="left:40px;top:47px"><span class="num">1</span><h3>We know firsthand 1</h3><span class="line" style="width:80px"></span>
    <div class="txt" style="width:80px">Since 1998, we have supported thousands of patients from the point of diagnosis through their journey with the disease.</div></div>
  <div class="item" style="left:40px;top:96px"><span class="num">2</span><h3>We know firsthand 2</h3><span class="line" style="width:80px"></span>
    <div class="txt" style="width:80px">We have supported thousands of patients from the point of diagnosis through their journey with the disease. we have supported thousands of patients from the point.</div></div>
  <div class="item" style="left:40px;top:153px"><span class="num">3</span><h3>We know firsthand 3</h3><span class="line" style="width:80px"></span>
    <div class="txt" style="width:80px">Since 1998, we have supported thousands of patients from the point of diagnosis through their journey.</div></div>
  <div class="item" style="left:157px;top:47px"><span class="num">4</span><h3>We know firsthand 4</h3><span class="line" style="width:80px"></span>
    <div class="txt" style="width:80px">Since 1998, we have supported thousands of patients from the point of diagnosis through their journey with the disease.</div></div>
  <div class="item" style="left:157px;top:96px"><span class="num">5</span><h3>We know firsthand 5</h3><span class="line" style="width:80px"></span>
    <div class="txt" style="width:80px">We have supported thousands of patients from the point of diagnosis through their journey with the disease. we have supported thousands of patients from the point.</div></div>
  <div class="item" style="left:157px;top:153px"><span class="num">6</span><h3>We know firsthand 6</h3><span class="line" style="width:80px"></span>
    <div class="txt" style="width:80px">Since 1998, we have supported thousands of patients from the point of diagnosis through their journey.</div></div>
  <div class="footer"><span class="page">4</span><span class="url">www.lumera-deck.com</span><span class="brand">LUMERA</span></div>
</section>

<!-- 7 world -->
<section class="slide c1 r3">
  <div class="title">More than 500+ satisfied client over the world</div>
  <div class="photo" role="img" aria-label="World map with client percentages per region" style="left:32px;top:45px;width:235px;height:130px;border-radius:40% 45% 35% 50%;background:radial-gradient(ellipse at 50% 45%,#8cc7ee,#b9ddf4 60%,#fff 75%)"></div>
  <div class="footer"><span class="page">5</span><span class="url">www.lumera-deck.com</span><span class="brand">LUMERA</span></div>
</section>

<!-- 8 divider -->
<section class="slide c2 r3 cover" style="background:linear-gradient(180deg,#5fb0e6,#2f8bd6 55%,#2a80cc)">
  <div class="brand">LUMERA</div>
  <div class="pill light" style="left:-40px;width:337px"></div>
  <h1 style="top:96px;color:var(--blue-deep)">YOUR DIVIDER PAGE HERE</h1>
  <h2 style="top:117px">YOUR PRESENTATION TITTLE HERE</h2>
  <div class="footer"><span class="page">6</span><span class="url">www.lumera-deck.com</span><span class="brand">LUMERA</span></div>
</section>

<!-- 9 mission 5 -->
<section class="slide c3 r3">
  <div class="title">Concept plus presentation powerful mission 5</div>
  <svg style="position:absolute;left:30px;top:50px" width="240" height="50" viewBox="0 0 240 50" font-family="Open Sans,sans-serif" font-size="4.2" fill="#fff" text-anchor="middle">
    <circle cx="218" cy="25" r="23" fill="#c4e3f6"/>
    <circle cx="172" cy="25" r="23" fill="#9fd1f1"/>
    <circle cx="126" cy="25" r="23" fill="#6bbbeb"/>
    <circle cx="80" cy="25" r="23" fill="#3f9fe0"/>
    <circle cx="34" cy="25" r="23" fill="#1e80cf"/>
    <text x="34" y="27">BRIEF</text><text x="80" y="27">ANALYSIS</text><text x="126" y="27">DESIGN</text><text x="172" y="27">DEVELOP</text><text x="218" y="27">TESTING</text>
  </svg>
  <div class="lead" style="top:118px">The LUMERA has myeloma research to a new level.</div>
  <div class="txt" style="left:28px;top:129px;width:240px">The pace at which lifesaving approach to the methodology of cancer research. By overcoming previous pitfalls that held the industry back, the HCRF has propelled the frontier of multiple myeloma research to a new level and new life-altering drugs can be brought to patients. By overcoming previous pitfalls that held the industry back, the HCRF has propelled the frontier of multiple myeloma research to a new level and new life-altering drugs can be brought to patients.</div>
  <div class="footer"><span class="page">7</span><span class="url">www.lumera-deck.com</span><span class="brand">LUMERA</span></div>
</section>

<!-- 10 mission 6 -->
<section class="slide c1 r4">
  <div class="title">Concept plus presentation powerful mission 6</div>
  <svg style="position:absolute;left:30px;top:40px" width="120" height="150" viewBox="0 0 120 150" font-family="Open Sans,sans-serif" font-size="4.2" fill="#fff" text-anchor="middle">
    <ellipse cx="60" cy="80" rx="58" ry="65" fill="#d3eaf8"/>
    <ellipse cx="60" cy="92" rx="50" ry="53" fill="#a8d5f2"/>
    <ellipse cx="60" cy="102" rx="42" ry="43" fill="#7cc0ec"/>
    <ellipse cx="60" cy="112" rx="34" ry="33" fill="#4ea8e3"/>
    <ellipse cx="60" cy="122" rx="26" ry="23" fill="#2a8fd8"/>
    <text x="60" y="24">BRIEF</text><text x="60" y="46">ANALYSIS</text><text x="60" y="67">DESIGN</text><text x="60" y="90">DEVELOP</text><text x="60" y="124">TESTING</text>
  </svg>
  <ul class="bullets">
    <li>Since 1998, we have supported</li><li>Essential to this approach reviews</li><li>Pitfalls that held the industry</li><li>Since 1998, we have supported</li><li>Essential to this approach reviews</li><li>Pitfalls that held the industry</li><li>Test has propelled the frontier</li><li>Multiple myeloma research to</li><li>Since 1998, we have supported</li><li>Essential to this approach reviews</li><li>Pitfalls that held the industry</li>
  </ul>
  <div class="footer"><span class="page">8</span><span class="url">www.lumera-deck.com</span><span class="brand">LUMERA</span></div>
</section>

<!-- 11 pie chart -->
<section class="slide c2 r4">
  <div class="title">Concept plus pie chart sample here</div>
  <div class="txt" style="left:37px;top:44px;width:100px">
    <p>The HCRF has forged a courageous and dynamic approach to the methodology of cancer research. By overcoming previous pitfalls that held the industry back, the HCRF has propelled the frontier of multiple myeloma research to a new level.</p>
    <p>Essential to this approach reviews pitfalls that held the industry back, the HCRF has propelled the frontier of multiple myeloma research to a new level are 4 groundbreaking initiatives that have revolutionized the way research and drug development are conducted. With these models, the HCRF can dramatically accelerate the pace at which lifesaving and new life-altering drugs can be brought to patients.</p>
  </div>
  <svg style="position:absolute;left:150px;top:70px" width="110" height="80" viewBox="0 0 110 80">
    <ellipse cx="55" cy="44" rx="48" ry="26" fill="#1667b0"/>
    <rect x="7" y="36" width="96" height="8" fill="#1667b0"/>
    <path d="M55 36 L55 10 A48 26 0 1 1 13.4 49 Z" fill="#1e80cf"/>
    <path d="M55 36 L13.4 49 A48 26 0 0 1 9.9 27.1 Z" fill="#9fd1f1"/>
    <path d="M55 36 L9.9 27.1 A48 26 0 0 1 31 13.5 Z" fill="#6bbbeb"/>
    <path d="M55 36 L31 13.5 A48 26 0 0 1 55 10 Z" fill="#c4e3f6"/>
  </svg>
  <div class="legend" style="left:150px;top:160px"><i style="background:#1e80cf"></i>Pie Chart 1<i style="background:#9fd1f1"></i>Pie Chart 2<i style="background:#6bbbeb"></i>Pie Chart 3<i style="background:#c4e3f6"></i>Pie Chart 4</div>
  <div class="footer"><span class="page">9</span><span class="url">www.lumera-deck.com</span><span class="brand">LUMERA</span></div>
</section>

<!-- 12 bar chart -->
<section class="slide c3 r4">
  <div class="title">Concept plus bar chart sample here</div>
  <div class="txt" style="left:37px;top:44px;width:100px">
    <p>The HCRF has forged a courageous and dynamic approach to the methodology of cancer research. By overcoming previous pitfalls that held the industry back, the HCRF has propelled the frontier of multiple myeloma research to a new level.</p>
    <p>Essential to this approach reviews pitfalls that held the industry back, the HCRF has propelled the frontier of multiple myeloma research to a new level are 4 groundbreaking initiatives that have revolutionized the way research and drug development are conducted. With these models, the HCRF can dramatically accelerate the pace at which lifesaving and new life-altering drugs can be brought to patients.</p>
  </div>
  <svg style="position:absolute;left:150px;top:40px" width="130" height="125" viewBox="0 0 130 125">
    <path d="M10 95 h14 l6 -4 h-14 z" fill="#d6ecf9"/><rect x="10" y="95" width="14" height="25" fill="#a9d6f2"/><path d="M24 95 l6 -4 v25 l-6 4 z" fill="#7dbce8"/>
    <path d="M32 80 h14 l6 -4 h-14 z" fill="#c4e3f6"/><rect x="32" y="80" width="14" height="40" fill="#7fc2ed"/><path d="M46 80 l6 -4 v40 l-6 4 z" fill="#4fa6e0"/>
    <path d="M54 60 h14 l6 -4 h-14 z" fill="#9fd1f1"/><rect x="54" y="60" width="14" height="60" fill="#4ea8e3"/><path d="M68 60 l6 -4 v60 l-6 4 z" fill="#2a86cf"/>
    <path d="M76 42 h14 l6 -4 h-14 z" fill="#6bbbeb"/><rect x="76" y="42" width="14" height="78" fill="#2a8fd8"/><path d="M90 42 l6 -4 v78 l-6 4 z" fill="#1667b0"/>
    <path d="M98 10 h14 l6 -4 h-14 z" fill="#4ea8e3"/><rect x="98" y="10" width="14" height="110" fill="#1e6fc0"/><path d="M112 10 l6 -4 v110 l-6 4 z" fill="#124f8e"/>
  </svg>
  <div class="legend" style="left:148px;top:170px"><i style="background:#a9d6f2"></i>Pie Chart 1<i style="background:#7fc2ed"></i>Pie Chart 2<i style="background:#4ea8e3"></i>Pie Chart 3<i style="background:#2a8fd8"></i>Pie Chart 4<i style="background:#1e6fc0"></i>Pie Chart 5</div>
  <div class="footer"><span class="page">10</span><span class="url">www.lumera-deck.com</span><span class="brand">LUMERA</span></div>
</section>

<!-- 13 table 1 -->
<section class="slide c1 r5">
  <div class="title">Concept plus table 1 sample here</div>
  <table style="left:38px;top:37px;width:215px">
    <tr><th>No</th><th>Name</th><th>Id Case</th><th>Address</th><th>Date</th><th>Case</th></tr>
    <tr><td>01.</td><td>Mr Alden Pike</td><td>#23091</td><td>Birch Lane 14a</td><td>17-06-13</td><td>Open</td></tr>
    <tr><td>02.</td><td>Mrs Nora Vale</td><td>#23092</td><td>Linden Street 14a</td><td>17-06-13</td><td>Open</td></tr>
    <tr><td>03.</td><td>Mr Alden Pike</td><td>#23093</td><td>Village Street 14a</td><td>17-06-13</td><td>Close</td></tr>
    <tr><td>04.</td><td>Mrs Nora Vale</td><td>#23094</td><td>Harbour Street 14a</td><td>17-06-13</td><td>Open</td></tr>
    <tr><td>05.</td><td>Mr Alden Pike</td><td>#23095</td><td>Birch Lane 14a</td><td>17-06-13</td><td>Open</td></tr>
  </table>
  <div class="lead" style="top:122px">The HCRF has myeloma research to a new level.</div>
  <div class="txt" style="left:34px;top:136px;width:230px">The pace at which lifesaving approach to the methodology of cancer research. By overcoming previous pitfalls that held the industry back, the HCRF has propelled the frontier of multiple myeloma research to a new level and new life-altering drugs can be brought to patients. By overcoming previous pitfalls that held the industry back.</div>
  <div class="footer"><span class="page">11</span><span class="url">www.lumera-deck.com</span><span class="brand">LUMERA</span></div>
</section>

<!-- 14 table 2 -->
<section class="slide c2 r5">
  <div class="title">Concept plus table 2 sample here</div>
  <div class="txt" style="left:37px;top:44px;width:100px">
    <p>The HCRF has forged a courageous and dynamic approach to the methodology of cancer research. By overcoming previous pitfalls that held the industry back, the HCRF has propelled the frontier of multiple myeloma research to a new level.</p>
    <p>Essential to this approach reviews pitfalls that held the industry back, the HCRF has propelled the frontier of multiple myeloma research to a new level are 4 groundbreaking initiatives that have revolutionized the way research and drug development are conducted. With these models, the HCRF can dramatically accelerate the pace at which lifesaving and new life-altering drugs can be brought to patients.</p>
  </div>
  <table style="left:145px;top:50px;width:118px">
    <tr><th>No</th><th>Name</th><th>Date</th><th>Case</th></tr>
    <tr><td>01.</td><td>Mr Alden Pike</td><td>17-06-13</td><td>Open</td></tr>
    <tr><td>02.</td><td>Mrs Nora Vale</td><td>17-06-13</td><td>Open</td></tr>
    <tr><td>03.</td><td>Mr Alden Pike</td><td>17-06-13</td><td>Close</td></tr>
    <tr><td>04.</td><td>Mrs Nora Vale</td><td>17-06-13</td><td>Open</td></tr>
    <tr><td>05.</td><td>Mr Alden Pike</td><td>17-06-13</td><td>Open</td></tr>
    <tr><td>06.</td><td>Mrs Nora Vale</td><td>17-06-13</td><td>Close</td></tr>
    <tr><td>07.</td><td>Mr Alden Pike</td><td>17-06-13</td><td>Open</td></tr>
    <tr><td>08.</td><td>Mrs Nora Vale</td><td>17-06-13</td><td>Open</td></tr>
  </table>
  <div class="footer"><span class="page">12</span><span class="url">www.lumera-deck.com</span><span class="brand">LUMERA</span></div>
</section>

<!-- 15 closing -->
<section class="slide c3 r5 cover">
  <div class="brand">LUMERA</div>
  <div class="pill" style="background:linear-gradient(180deg,#a9d6f2,#5fb0e6)"></div>
  <h1 style="top:95px">THANK YOU FOR ATTENTION</h1>
  <h2 style="top:117px">YOUR PRESENTATION TITTLE HERE</h2>
  <div class="small" style="top:190px;line-height:5.5px">© 2013 Lumera<br>All rights reserved</div>
</section>

</main>
</body>
</html>
```